Website for The Tavery Parlour

I require a website for "The Tavery Parlour" which is a blog type business for 40+ year old women covering books, true crime, history, travel and food. It needs to support blog posts, links to social media including YouTube videos, Instagram, TikTok and Facebook. The background theme needs to be like that of a newspaper. Easy to navigate and to allow me to post blogs/videos.

```html
<!DOCTYPE html>
<html lang="en">
<head>
<meta charset="utf-8">
<title>The Tavery Parlour</title>
<link href="https://fonts.googleapis.com/css2?family=Merriweather:wght@400;700;900&family=Inter:wght@400;500;600&display=swap" rel="stylesheet">
<style>
:root{
  --red:#c8283a;
  --ink:#1f1f1f;
  --dark:#2c2b2a;
  --paper:#f0eae2;
  --paper-2:#e9e2d8;
  --card:#f7f4f0;
  --muted:#8a8682;
  --line:#dcd6ce;
  --white:#ffffff;
}
*{box-sizing:border-box;margin:0;padding:0}
html,body{width:1200px;height:3741px;overflow:hidden}
body{position:relative;background:var(--white);font-family:"Inter",sans-serif;color:var(--ink)}
.abs{position:absolute}
section,header,footer{position:absolute;left:0;width:1200px}
.ph{position:absolute;overflow:hidden}

/* header */
.site-header{top:0;height:75px;background:var(--white)}
.brand{position:absolute;left:157px;top:18px;font-family:"Merriweather",serif;font-weight:700;font-size:30px;color:var(--ink);letter-spacing:-0.5px;white-space:nowrap}
.btn{display:inline-block;background:var(--red);color:var(--white);font-family:"Merriweather",serif;font-size:11px;letter-spacing:.5px;text-transform:uppercase;border-radius:4px;text-align:center;white-space:nowrap}
.talk{position:absolute;left:943px;top:26px;width:100px;height:31px;line-height:31px}
.nav-band{top:75px;height:44px}
.nav-red{position:absolute;left:0;top:0;width:870px;height:34px;background:var(--red);clip-path:polygon(0 0,857px 0,870px 34px,0 34px)}
.nav-dark{position:absolute;left:857px;top:9px;width:343px;height:35px;background:var(--dark);clip-path:polygon(0 0,343px 0,343px 35px,14px 35px)}
.nav{position:absolute;left:157px;top:3px;display:flex;list-style:none}
.nav li{font-family:"Merriweather",serif;font-size:11px;color:var(--white);text-transform:uppercase;height:28px;line-height:28px;padding:0 13px;margin-right:16px;letter-spacing:.4px;white-space:nowrap}
.nav li.active{background:var(--dark);border-radius:3px}
.social{position:absolute;display:flex;gap:18px}
.social span{display:block;width:14px;height:14px;border-radius:3px;background:var(--white)}
.nav-dark .social{left:66px;top:11px}

/* hero */
.hero{top:109px;height:455px;background:linear-gradient(180deg,#c9a27f 0%,#a57a5a 35%,#6e5a4c 70%,#3f342d 100%)}
.hero-text{position:absolute;left:176px;top:128px;color:var(--white)}
.hero-date{font-family:"Merriweather",serif;font-size:10px;display:flex;align-items:center;gap:6px}
.hero h1{font-family:"Merriweather",serif;font-weight:900;font-size:28px;line-height:38px;margin-top:14px;text-transform:uppercase;letter-spacing:.3px;white-space:nowrap}
.hero .btn{margin-top:18px;width:104px;height:29px;line-height:29px}
.dots{position:absolute;left:1026px;top:178px;display:flex;flex-direction:column;gap:8px}
.dots i{display:block;width:10px;height:10px;border:1.5px solid var(--white);border-radius:50%}
.dots i.on{background:var(--red);border-color:var(--red)}

/* blog */
.blog{top:564px;height:1288px;background:radial-gradient(circle at 30% 20%,#f6f1ea 0%,var(--paper) 60%,var(--paper-2) 100%)}
.post{position:absolute}
.post .thumb{position:absolute;left:0;top:0;border-radius:3px}
.tag{position:absolute;left:10px;top:7px;background:#111;color:var(--white);font-family:"Merriweather",serif;font-size:9px;padding:2px 6px;border-radius:2px}
.meta{position:absolute;left:0;display:flex;align-items:center;gap:7px;font-family:"Merriweather",serif;font-size:9.5px;color:#444;white-space:nowrap}
.ptitle{position:absolute;left:0;font-family:"Merriweather",serif;font-weight:700;font-size:12.5px;line-height:20px;color:var(--ink);white-space:nowrap}
.excerpt{position:absolute;left:0;font-size:10px;line-height:19px;color:var(--muted);white-space:nowrap}
.stats{position:absolute;left:0;display:flex;align-items:center;font-size:10px;color:var(--muted)}
.stats .st{display:flex;align-items:center;gap:4px;padding-right:10px;margin-right:10px;border-right:1px solid var(--line)}
.stats .st:last-child{border-right:0}
svg.ic{width:15px;height:15px;stroke:var(--red);fill:none;stroke-width:1.5}
.sidebar-box{position:absolute;left:806px;width:237px;background:var(--card);border-radius:4px}
.sidebar-box h3{font-family:"Merriweather",serif;font-size:15px;color:var(--red);position:absolute;left:13px;top:12px}
.rp{position:absolute;left:13px;width:212px}
.rp .ph{left:0;top:0;width:58px;height:58px;border-radius:4px}
.rp p{position:absolute;left:72px;top:0;font-family:"Merriweather",serif;font-size:9px;line-height:15px;color:var(--ink);white-space:nowrap}
.rp small{position:absolute;left:72px;top:49px;font-family:"Merriweather",serif;font-size:9px;color:var(--muted);white-space:nowrap}
.rp-sep{position:absolute;left:13px;width:212px;height:1px;background:var(--line)}
.tags{position:absolute;left:15px;top:41px;width:210px;display:flex;flex-wrap:wrap;gap:8px 8px}
.tags span{font-family:"Merriweather",serif;font-size:9px;border:1px solid var(--line);background:var(--white);padding:3px 8px;border-radius:2px}
.pager{position:absolute;left:157px;top:1189px;display:flex;gap:8px}
.pager span{display:block;min-width:24px;height:24px;line-height:22px;text-align:center;border:1px solid var(--line);background:var(--white);font-size:11px;border-radius:3px;padding:0 6px}
.pager span.on{background:var(--red);color:var(--white);border-color:var(--red)}

/* what we do */
.what{top:1852px;height:542px;background:linear-gradient(180deg,#333230,#2a2928)}
.kicker{font-family:"Merriweather",serif;font-size:10px;color:var(--red);text-transform:uppercase;letter-spacing:.6px}
.h2{font-family:"Merriweather",serif;font-weight:700;font-size:20px;line-height:30px;white-space:nowrap}
.what .kicker{position:absolute;left:157px;top:74px}
.what .h2{position:absolute;left:157px;top:100px;color:var(--white)}
.what p{position:absolute;left:657px;top:350px;width:390px;font-size:10.5px;line-height:19px;color:#ddd}
.what .btn{position:absolute;left:657px;top:439px;width:104px;height:29px;line-height:29px}

/* videos */
.videos{top:2394px;height:555px;background:radial-gradient(circle at 60% 40%,#f5f0e9,var(--paper))}
.videos .kicker{position:absolute;left:157px;top:76px}
.videos .h2{position:absolute;left:157px;top:102px}
.arrow{position:absolute;top:112px;width:27px;height:27px;border-radius:50%;display:flex;align-items:center;justify-content:center}
.arrow svg{width:12px;height:12px;stroke:var(--white);fill:none;stroke-width:2.2}
.vid{position:absolute;top:179px;width:193px;height:299px;border-radius:3px}
.play{position:absolute;left:50%;top:50%;width:32px;height:32px;margin:-16px 0 0 -16px;border-radius:50%;background:rgba(30,30,30,.75);display:flex;align-items:center;justify-content:center}
.play svg{width:12px;height:12px;fill:var(--red);margin-left:2px}

/* best choice */
.best{top:2949px;height:506px;background:var(--white)}
.best .kicker{position:absolute;left:0;width:1200px;text-align:center;top:75px}
.best .h2{position:absolute;left:0;width:1200px;text-align:center;top:96px}
.mini{position:absolute;left:204px;width:210px}
.mini .ph{left:0;top:0;width:58px;height:58px;border-radius:4px}
.mini p{position:absolute;left:72px;top:0;font-family:"Merriweather",serif;font-size:9px;line-height:15px;white-space:nowrap}
.mini small{position:absolute;left:72px;top:49px;font-family:"Merriweather",serif;font-size:9px;color:var(--muted);white-space:nowrap}
.feature{position:absolute;left:449px;top:145px;width:550px;height:279px;background:var(--card);border-radius:3px}

/* newsletter */
.news{top:3455px;height:203px;background:linear-gradient(180deg,#2f2e2c,#262524)}
.news .kicker{position:absolute;left:0;width:1200px;text-align:center;top:55px}
.news .h2{position:absolute;left:0;width:1200px;text-align:center;top:75px;color:var(--white)}
.subscribe{position:absolute;left:401px;top:110px;width:397px;height:35px;background:var(--white);border-radius:5px}
.subscribe .field{position:absolute;left:12px;top:11px;font-size:10px;color:var(--muted)}
.subscribe .signup{position:absolute;right:3px;top:3px;width:82px;height:29px;line-height:29px}

/* footer */
.site-footer{top:3658px;height:83px;background:var(--white)}
.copy{position:absolute;left:157px;top:35px;font-size:10px;color:var(--ink)}
.site-footer .brand{left:0;width:1200px;text-align:center;top:21px;font-size:26px}
.site-footer .social{left:932px;top:35px}
.site-footer .social span{background:var(--ink)}
</style>
</head>
<body>
<svg width="0" height="0" style="position:absolute" aria-hidden="true">
  <defs>
    <symbol id="i-cal" viewBox="0 0 16 16"><rect x="2" y="3" width="12" height="11" rx="1"/><path d="M2 6.5h12M5 1.5v3M11 1.5v3"/></symbol>
    <symbol id="i-com" viewBox="0 0 16 16"><path d="M8 2a6 6 0 1 0 3.2 11.1L14 14l-.9-2.7A6 6 0 0 0 8 2z"/><path d="M5 8h.01M8 8h.01M11 8h.01"/></symbol>
    <symbol id="i-like" viewBox="0 0 16 16"><path d="M2 7h3v7H2zM5 7l3-5c1.2 0 1.8.8 1.6 2L9.2 6H13a1.3 1.3 0 0 1 1.3 1.5l-1 5.4A1.3 1.3 0 0 1 12 14H5"/></symbol>
    <symbol id="i-vid" viewBox="0 0 16 16"><rect x="2" y="2.5" width="12" height="9" rx="1"/><path d="M7 5v4l3-2zM5 14h6"/></symbol>
    <symbol id="i-share" viewBox="0 0 16 16"><circle cx="12" cy="3.5" r="2"/><circle cx="4" cy="8" r="2"/><circle cx="12" cy="12.5" r="2"/><path d="M5.8 7l4.4-2.5M5.8 9l4.4 2.5"/></symbol>
  </defs>
</svg>

<header class="site-header">
  <div class="brand">The Tavery Parlour</div>
  <span class="btn talk">Let's Talk</span>
</header>

<div class="abs nav-band" style="left:0;width:1200px">
  <div class="nav-red">
    <ul class="nav">
      <li class="active">Home</li><li>About Us</li><li>Books</li><li>True Crime</li><li>History</li><li>Travel</li><li>Food</li>
    </ul>
  </div>
  <div class="nav-dark">
    <div class="social" aria-label="Social links"><span aria-label="Social profile 1"></span><span aria-label="Social profile 2"></span><span aria-label="Social profile 3"></span><span aria-label="Social profile 4"></span></div>
  </div>
</div>

<section class="hero" role="img" aria-label="Traveller with backpack and open arms on a cliff above a bay at sunset">
  <div class="hero-text">
    <div class="hero-date"><svg class="ic" style="width:13px;height:13px"><use href="#i-cal"/></svg>Aug 4, 2025</div>
    <h1>Lorem Ipsum Is Simply<br>Dummy Text Of The<br>Printing Industry.</h1>
    <span class="btn">Read More</span>
  </div>
  <div class="dots"><i></i><i></i><i class="on"></i><i></i></div>
</section>

<section class="blog">
  <div class="post" style="left:157px;top:75px;width:299px">
    <div class="ph thumb" style="width:299px;height:177px;background:linear-gradient(135deg,#5a3a24,#b89670 55%,#3b2a1e)" role="img" aria-label="Hands holding an open book"></div>
    <span class="tag">Books</span>
    <div class="meta" style="top:200px"><svg class="ic"><use href="#i-cal"/></svg>Aug 4, 2025</div>
    <div class="ptitle" style="top:222px">Lorem Ipsum Is Simply Dummy Text<br>Of The Printing Industry.</div>
    <div class="excerpt" style="top:265px">Lorem Ipsum Is Simply Dummy Text Of The Printing<br>And Typesetting Industry...</div>
    <div class="stats" style="top:314px"><span class="st"><svg class="ic"><use href="#i-com"/></svg>34</span><span class="st"><svg class="ic"><use href="#i-like"/></svg>56</span><span class="st"><svg class="ic"><use href="#i-share"/></svg></span></div>
  </div>
  <div class="post" style="left:481px;top:75px;width:301px">
    <div class="ph thumb" style="width:301px;height:177px;background:linear-gradient(90deg,#6b4a33 0%,#6b4a33 12%,#e7a9bd 12%,#e7a9bd 85%,#5c3f2c 85%)" role="img" aria-label="Pink true crime book cover on a wooden table"></div>
    <span class="tag">True Crime</span>
    <div class="meta" style="top:200px"><svg class="ic"><use href="#i-cal"/></svg>Aug 4, 2025</div>
    <div class="ptitle" style="top:222px">Lorem Ipsum Is Simply Dummy Text<br>Of The Printing Industry.</div>
    <div class="excerpt" style="top:265px">Lorem Ipsum Is Simply Dummy Text Of The Printing<br>And Typesetting Industry...</div>
    <div class="stats" style="top:314px"><span class="st"><svg class="ic"><use href="#i-com"/></svg>34</span><span class="st"><svg class="ic"><use href="#i-like"/></svg>56</span><span class="st"><svg class="ic"><use href="#i-vid"/></svg></span><span class="st"><svg class="ic"><use href="#i-share"/></svg></span></div>
  </div>
  <div class="post" style="left:157px;top:437px;width:625px">
    <div class="ph thumb" style="width:625px;height:250px;background:linear-gradient(100deg,#c9a46a 0%,#7aa6d4 35%,#a9c9e8 70%,#e3e7ea 100%)" role="img" aria-label="Two women in sunhats near a harbour opera house"></div>
    <span class="tag">Travel</span>
    <div class="meta" style="top:277px"><svg class="ic"><use href="#i-cal"/></svg>Aug 4, 2025</div>
    <div class="ptitle" style="top:300px">Lorem Ipsum Is Simply Dummy Text Of The Printing Industry.</div>
    <div class="excerpt" style="top:322px">Lorem Ipsum Is Simply Dummy Text Of The Printing And Typesetting Industry...</div>
    <div class="stats" style="top:355px"><span class="st"><svg class="ic"><use href="#i-com"/></svg>34</span><span class="st"><svg class="ic"><use href="#i-like"/></svg>56</span><span class="st"><svg class="ic"><use href="#i-vid"/></svg></span><span class="st"><svg class="ic"><use href="#i-share"/></svg></span></div>
  </div>
  <div class="post" style="left:157px;top:831px;width:190px">
    <div class="ph thumb" style="width:190px;height:177px;background:linear-gradient(135deg,#a88a62,#6a5238 60%,#3e3022)" role="img" aria-label="Old maps with a mask and a bowl"></div>
    <span class="tag">History</span>
    <div class="meta" style="top:193px"><svg class="ic"><use href="#i-cal"/></svg>Aug 4, 2025</div>
    <div class="ptitle" style="top:217px">Lorem Ipsum Is Simply<br>Dummy Text Of The<br>Printing Industry.</div>
    <div class="stats" style="top:285px"><span class="st"><svg class="ic"><use href="#i-com"/></svg>34</span><span class="st"><svg class="ic"><use href="#i-like"/></svg>56</span><span class="st"><svg class="ic"><use href="#i-share"/></svg></span></div>
  </div>
  <div class="post" style="left:372px;top:831px;width:192px">
    <div class="ph thumb" style="width:192px;height:177px;background:linear-gradient(135deg,#e0a43a,#b86b1c 55%,#7a3e10)" role="img" aria-label="Golden glazed pastries"></div>
    <span class="tag">Food</span>
    <div class="meta" style="top:193px"><svg class="ic"><use href="#i-cal"/></svg>Aug 4, 2025</div>
    <div class="ptitle" style="top:217px">Lorem Ipsum Is Simply<br>Dummy Text Of The<br>Printing Industry.</div>
    <div class="stats" style="top:285px"><span class="st"><svg class="ic"><use href="#i-com"/></svg>34</span><span class="st"><svg class="ic"><use href="#i-like"/></svg>56</span><span class="st"><svg class="ic"><use href="#i-share"/></svg></span></div>
  </div>
  <div class="post" style="left:588px;top:831px;width:192px">
    <div class="ph thumb" style="width:192px;height:177px;background:linear-gradient(100deg,#c9a46a,#7aa6d4 55%,#b6cfe6)" role="img" aria-label="Women in sunhats on a sunny trip"></div>
    <span class="tag">Books</span>
    <div class="meta" style="top:193px"><svg class="ic"><use href="#i-cal"/></svg>Aug 4, 2025</div>
    <div class="ptitle" style="top:217px">Lorem Ipsum Is Simply<br>Dummy Text Of The<br>Printing Industry.</div>
    <div class="stats" style="top:285px"><span class="st"><svg class="ic"><use href="#i-com"/></svg>34</span><span class="st"><svg class="ic"><use href="#i-like"/></svg>56</span><span class="st"><svg class="ic"><use href="#i-vid"/></svg></span><span class="st"><svg class="ic"><use href="#i-share"/></svg></span></div>
  </div>

  <div class="pager"><span>1</span><span class="on">2</span><span>3</span><span>Next</span></div>

  <aside class="sidebar-box" style="top:75px;height:327px">
    <h3>Recent Post</h3>
    <div class="rp" style="top:50px"><div class="ph" style="background:linear-gradient(135deg,#c6452a,#e9b04a 50%,#3d6b2e)" role="img" aria-label="Rice and vegetable dish"></div><p>Lorem Ipsum Is Dummy<br>Text Of The Printing And<br>Typesetting...</p><small>Aug 4, 2025</small></div>
    <div class="rp-sep" style="top:131px"></div>
    <div class="rp" style="top:147px"><div class="ph" style="background:linear-gradient(135deg,#a07a50,#b8322a 60%,#3a4a5a)" role="img" aria-label="Traveller sitting with a red backpack"></div><p>Lorem Ipsum Is Dummy<br>Text Of The Printing And<br>Typesetting...</p><small>Aug 4, 2025</small></div>
    <div class="rp-sep" style="top:228px"></div>
    <div class="rp" style="top:244px"><div class="ph" style="background:linear-gradient(135deg,#c6452a,#e9b04a 50%,#3d6b2e)" role="img" aria-label="Rice and vegetable dish"></div><p>Lorem Ipsum Is Dummy<br>Text Of The Printing And<br>Typesetting...</p><small>Aug 4, 2025</small></div>
  </aside>
  <aside class="sidebar-box" style="top:428px;height:108px">
    <h3>Tags</h3>
    <div class="tags"><span>Books</span><span>True Crime</span><span>History</span><span>Travel</span><span>Food</span></div>
  </aside>
</section>

<section class="what">
  <div class="kicker">What We Do</div>
  <div class="h2">Lorem Ipsum Is Simply Dummy Text<br>Of The Printing Industry.</div>
  <div class="ph" style="left:157px;top:182px;width:430px;height:286px;background:linear-gradient(180deg,#d8c3a0 0%,#8fb3c9 45%,#2e6f93 100%)" role="img" aria-label="Harbour opera house and city skyline at sunrise"></div>
  <div class="ph" style="left:657px;top:74px;width:386px;height:256px;background:linear-gradient(120deg,#c7d9e3,#e9eef0 50%,#9fb8d4)" role="img" aria-label="Smiling woman in a hat on the phone holding a passport"></div>
  <p>Lorem Ipsum Is Simply Dummy Text Of The Printing And Typesetting Industry. Lorem Ipsum Has Been The Industry's Standard Dummy Text Ever Since The 1500s, When An Unknown Printer Took A Galley Of Type And Scrambled It To Make A Type Specimen Book.</p>
  <span class="btn">Read More</span>
</section>

<section class="videos">
  <div class="kicker">Short Videos</div>
  <div class="h2">Lorem Ipsum Is Simply Dummy Text<br>Of The Printing Industry.</div>
  <div class="arrow" style="left:981px;background:#c9c5c1"><svg viewBox="0 0 12 12"><path d="M8 2L4 6l4 4"/></svg></div>
  <div class="arrow" style="left:1016px;background:var(--red)"><svg viewBox="0 0 12 12"><path d="M4 2l4 4-4 4"/></svg></div>
  <div class="ph vid" style="left:157px;background:linear-gradient(160deg,#8a5a38,#d7b17a 45%,#c14a2a)" role="img" aria-label="Plate of rice with curry and salad"><span class="play"><svg viewBox="0 0 12 12"><path d="M2 1l9 5-9 5z"/></svg></span></div>
  <div class="ph vid" style="left:375px;background:linear-gradient(160deg,#5a3e26,#c9a26c 50%,#7a5534)" role="img" aria-label="Ancient scroll with written characters"><span class="play"><svg viewBox="0 0 12 12"><path d="M2 1l9 5-9 5z"/></svg></span></div>
  <div class="ph vid" style="left:594px;background:linear-gradient(180deg,#9fb0bf,#6f7f72 55%,#4a3a4a)" role="img" aria-label="Hiker pointing across a valley"><span class="play"><svg viewBox="0 0 12 12"><path d="M2 1l9 5-9 5z"/></svg></span></div>
  <div class="ph vid" style="left:812px;background:linear-gradient(160deg,#2a2a26,#b9873e 50%,#5a2a2a)" role="img" aria-label="Bowl of stir fried noodles with vegetables"><span class="play"><svg viewBox="0 0 12 12"><path d="M2 1l9 5-9 5z"/></svg></span></div>
  <div class="ph vid" style="left:1031px;width:169px;border-radius:3px 0 0 3px;background:linear-gradient(160deg,#d9cbb4,#7a6a5a 50%,#b7322a)" role="img" aria-label="Traveller working on a laptop beside a red backpack"><span class="play" style="left:96px"><svg viewBox="0 0 12 12"><path d="M2 1l9 5-9 5z"/></svg></span></div>
</section>

<section class="best">
  <div class="kicker">Best Choice</div>
  <div class="h2">Most Interesting</div>
  <div class="mini" style="top:156px"><div class="ph" style="background:linear-gradient(135deg,#c6452a,#e9b04a 50%,#3d6b2e)" role="img" aria-label="Rice and vegetable dish"></div><p>Lorem Ipsum Is Dummy<br>Text Of The Printing And<br>Typesetting...</p><small>Aug 4, 2025</small></div>
  <div class="mini" style="top:253px"><div class="ph" style="background:linear-gradient(135deg,#5a3e26,#c9a26c 50%,#7a5534)" role="img" aria-label="Ancient scroll"></div><p>Lorem Ipsum Is Dummy<br>Text Of The Printing And<br>Typesetting...</p><small>Aug 4, 2025</small></div>
  <div class="mini" style="top:350px"><div class="ph" style="background:linear-gradient(135deg,#c6452a,#e9b04a 50%,#3d6b2e)" role="img" aria-label="Rice and vegetable dish"></div><p>Lorem Ipsum Is Dummy<br>Text Of The Printing And<br>Typesetting...</p><small>Aug 4, 2025</small></div>
  <div class="feature">
    <div class="ph" style="left:0;top:0;width:237px;height:279px;background:linear-gradient(150deg,#2a1c12,#8a5a34 50%,#3a2616)" role="img" aria-label="Carved wooden tribal mask"></div>
    <div class="meta" style="left:263px;top:80px"><svg class="ic"><use href="#i-cal"/></svg>Aug 4, 2025</div>
    <div class="ptitle" style="left:263px;top:104px">Lorem Ipsum Is Simply Dummy<br>Text Of The Printing Industry.</div>
    <div class="excerpt" style="left:263px;top:146px">Lorem Ipsum Is Simply Dummy Text Of The<br>Printing And Typesetting Industry...</div>
    <div class="stats" style="left:263px;top:197px"><span class="st"><svg class="ic"><use href="#i-com"/></svg>34</span><span class="st"><svg class="ic"><use href="#i-like"/></svg>56</span><span class="st"><svg class="ic"><use href="#i-vid"/></svg></span><span class="st"><svg class="ic"><use href="#i-share"/></svg></span></div>
  </div>
</section>

<section class="news">
  <div class="kicker">Newsletter Signup</div>
  <div class="h2">Subscribe For The Updates!</div>
  <div class="subscribe"><span class="field">Enter Email</span><span class="btn signup">Sign Up</span></div>
</section>

<footer class="site-footer">
  <div class="copy">© 2025 The Tavery Parlour. All Right Reserved</div>
  <div class="brand">The Tavery Parlour</div>
  <div class="social" aria-label="Social links"><span aria-label="Social profile 1"></span><span aria-label="Social profile 2"></span><span aria-label="Social profile 3"></span><span aria-label="Social profile 4"></span></div>
</footer>
</body>
</html>
```